PLV Flyer

We need a professional design for flyers that we produce. The attached event draft is typical of the majority of flyers we will produce, and is the one that we need to do right now.

We would also like the source files for the design. We don’t have Corel Draw, but can work with any files produced in Adobe Creative Suite products.

Target Market(s)

Owners of residential apartments

Industry/Entity Type

Non-Profit

Requirements
Must have
• Design must be complimentary to our new website design at www.plv.org.au so we can establish consistent branding.
• Any fonts used must be freely avalaible standard fonts used in Microsoft Word

```html
<!DOCTYPE html>
<html lang="en">
<head>
<meta charset="utf-8">
<title>PLV Educational Workshop</title>
<link href="https://fonts.googleapis.com/css2?family=Arimo:ital,wght@0,400;0,700;1,700&family=Roboto+Condensed:wght@700&display=swap" rel="stylesheet">
<style>
:root{
  --navy:#1f3b7e;
  --heading:#23418c;
  --gold:#e3a82f;
  --gold-dark:#cf9628;
  --table-blue:#2262b2;
  --ink:#1d1d1d;
  --muted:#5a5a5a;
  --panel:#f0f0f0;
  --panel-dark:#dcdde1;
  --register:#dfe0e3;
  --white:#ffffff;
}
*{margin:0;padding:0;box-sizing:border-box}
html,body{width:849px;height:1200px;overflow:hidden;background:var(--white)}
body{font-family:"Arimo",Arial,sans-serif;color:var(--ink)}
.flyer{position:relative;width:849px;height:1200px;overflow:hidden;background:var(--white)}
.abs{position:absolute}
.brand{left:40px;top:82px;display:flex;align-items:center;gap:14px}
.brand-square{width:36px;height:36px;background:var(--gold)}
.brand-name{font-family:"Arimo",Arial,sans-serif;font-weight:400;font-size:33px;line-height:32px;letter-spacing:2px;color:var(--navy);text-transform:uppercase}
.hero-photo{left:538px;top:0;width:311px;height:203px;background:linear-gradient(120deg,#c9c3bb,#e8e4df 45%,#f4f3f1)}
.title-band{left:0;top:205px;width:849px;height:55px;background:linear-gradient(var(--gold) 60%,var(--gold-dark));color:var(--white);text-align:center;font-weight:700;font-size:24px;line-height:58px}
.subtitle-band{left:0;top:263px;width:849px;height:30px;background:var(--navy);color:var(--white);text-align:center;font-style:italic;font-weight:700;font-size:14px;letter-spacing:1.6px;line-height:30px}
.gold-rule{left:0;top:295px;width:849px;height:3px;background:var(--gold)}
.photo-frame{left:18px;top:317px;width:322px;height:469px;background:var(--white);border:1px solid #cfcfcf;box-shadow:3px 4px 8px rgba(0,0,0,.25);transform:rotate(-0.6deg)}
.photo-fill{position:absolute;left:8px;top:8px;right:8px;bottom:9px;background:linear-gradient(135deg,#bfcde0,#e9edf2 50%,#8a9bb3)}
.intro{left:373px;top:330px;width:460px}
.condensed{font-family:"Roboto Condensed","Arial Narrow",sans-serif;font-weight:700;color:var(--heading)}
.intro h2{font-size:17px;line-height:26px}
.intro ul{list-style:none;font-size:12px;margin-top:8px}
.intro li{line-height:25.5px}
.intro li::before{content:"• "}
.intro .particular{font-size:13px;margin:4px 0 4px 10px;line-height:24px}
.intro .wrap{line-height:20px;padding-left:9px;text-indent:-9px}
.facts{left:373px;top:515px;width:470px;font-size:12px}
.fact{line-height:28.6px}
.fact .label{font-size:16px;margin-right:2px}
.register{left:368px;top:659px;width:481px;height:30px;background:var(--register);padding-left:5px;font-size:16px;line-height:31px;letter-spacing:.4px}
.programme{left:373px;top:693px;width:430px;font-size:12px;line-height:25.8px}
.programme .label{font-size:16px}
.lower{left:0;top:818px;width:849px;height:334px;background:var(--panel);border-top:1px solid #999}
.theme{left:32px;top:840px;width:800px}
.theme h3{font-size:16px;line-height:26px;margin-bottom:2px}
.theme p{font-size:12px;line-height:24.3px;color:var(--muted)}
.theme .reserve{float:right;width:502px;height:200px}
.schedule{left:330px;top:818px;width:519px;height:222px;background:var(--panel-dark);border-left:1px solid #999;border-bottom:1px solid #999}
.schedule h3{position:absolute;left:13px;top:15px;font-size:16px}
.schedule table{position:absolute;left:10px;top:48px;width:495px;border-collapse:separate;border-spacing:0;background:var(--white);border:1px solid #555;border-radius:14px;overflow:hidden;font-size:12px}
.schedule th{background:var(--table-blue);color:var(--white);font-weight:700;height:28px;border-left:1px solid #333}
.schedule th:first-child{border-left:0}
.schedule td{padding:0 9px;border-left:1px solid #555;border-top:1px solid #555;vertical-align:middle}
.schedule td.period{border-left:0}
.schedule .r1{height:27px}
.schedule .r2{height:51px}
.schedule .r2 td{line-height:21px}
.schedule .r3{height:25px}
.schedule .r4{height:29px}
.footer-band{left:0;top:1152px;width:849px;height:48px;background:linear-gradient(var(--gold) 60%,var(--gold-dark));color:var(--white);text-align:center;font-family:"Roboto Condensed","Arial Narrow",sans-serif;font-weight:700;font-size:16px;line-height:50px}
</style>
</head>
<body>
<main class="flyer">
  <div class="abs brand">
    <span class="brand-square"></span>
    <span class="brand-name">Property<br>Living<br>Victoria</span>
  </div>
  <div class="abs hero-photo" role="img" aria-label="Photo of four smiling young professionals seated in a row"></div>

  <h1 class="abs title-band">PLV Educational Workshop</h1>
  <div class="abs subtitle-band">“The Essentials of Strata Living – What Every Owner Needs to Know” 12th and 26th June 2010</div>
  <div class="abs gold-rule"></div>

  <div class="abs photo-frame"><div class="photo-fill" role="img" aria-label="Photo of three colleagues looking at a document on a table"></div></div>

  <section class="abs intro">
    <h2 class="condensed">This Workshop Is For Owners In Strata Apartments Who Want To Learn More About:</h2>
    <ul>
      <li>getting the best out of apartment living</li>
      <li>protecting their home and their investment</li>
    </ul>
    <p class="particular condensed">AND particularly for...</p>
    <ul>
      <li class="wrap">executive committee members to know their rights<br>&nbsp;and responsibilities in managing their strata scheme</li>
    </ul>
  </section>

  <section class="abs facts">
    <p class="fact"><span class="label condensed">Location:</span> Harbourside Club 24 Wharf Street Bayview 2099</p>
    <p class="fact"><span class="label condensed">Dates:</span> The workshop will run twice – on 12th June and 26th June 2010</p>
    <p class="fact"><span class="label condensed">Time:</span> 10.00 am to 4.00 pm.</p>
    <p class="fact"><span class="label condensed">Cost:</span> $60.00, which includes morning tea and lunch.</p>
    <p style="line-height:20px">The maximum number of participants for each workshop is 60.</p>
  </section>

  <div class="abs register condensed">Register Online at: www.plv.org.au</div>

  <p class="abs programme"><span class="label condensed">Programme:</span> The day will comprise four sessions, each facilitated by a specialist. In each session the speaker will provide relevant information and set the topics for group work; participants will break into groups and work up solutions to each topic; and the groups will compare outcomes.</p>

  <div class="abs lower"></div>

  <section class="abs theme">
    <h3 class="condensed">The Day’s Theme Will Be:</h3>
    <p><span class="reserve"></span>Gina is a new owner in her building called Meridian Tower. She notices some management processes which to her seem strange. She is elected to the executive committee and finds that the developer has retained more control than she realised - the service providers have long-term and onerous contracts, and she doesn’t seem to be able to exert enough influence. What does the law require her to do, as a committee member? How does she influence good management processes? The finances seem to be out of control, so how can she fix them so she doesn’t pay inflated levies each year and lose value on her investment? ... and then the neighbour above her apartment installs a timber floor and she has noise problems ... and the building seems to have a lot of defects ............</p>
  </section>

  <section class="abs schedule">
    <h3 class="condensed">Conference Schedule:</h3>
    <table>
      <colgroup><col style="width:80px"><col style="width:144px"><col></colgroup>
      <thead><tr><th></th><th>Topic</th><th>Speaker</th></tr></thead>
      <tbody>
        <tr class="r1"><td class="period" rowspan="2">Morning</td><td>Governance</td><td>Martin Hale, strata lawyer</td></tr>
        <tr class="r2"><td>Management</td><td>Simon Weller, seasoned former chairperson and executive committee member</td></tr>
        <tr class="r3"><td class="period" rowspan="2">Afternoon</td><td>Financials</td><td>Peter Landry, accountant</td></tr>
        <tr class="r4"><td>Physicality</td><td>Daniel Ferris, facilities manager</td></tr>
      </tbody>
    </table>
  </section>

  <div class="abs footer-band">Enroll Now - Learn A Lot - Have Some Fun As Well - Share Experiences - Find Out How PLV Can Help You In The Longer Term</div>
</main>
</body>
</html>
```